Business Card Design - Corporate

Create a sleek elegant business card layout while suggesting a color scheme. Convey cutting edge technology while maintaining a corporate feel that is easily readable.

Company designs and manufactures consumer electronic products for mass retail that are mainly app driven.

(vector logo and die-line provided)

Target Market(s)

Corporate level, tech industry.

Industry/Entity Type

Business

Contact Information for Business Card

Generic Info:

Name
Title
email
address
phone 1
phone 2
website (quillbarn.com) on back

Font styles to use
Sans Serif

Requirements
Must have
• At least 2 colors + white on one side.
Nice to have
• Solid suggestion on color for logo and overall design. Color flood on back of card.
Should not have
• background texture like... marble, stone, patterns or circuit boards

```html
<!DOCTYPE html>
<html lang="en">
<head>
<meta charset="utf-8">
<title>Quillbarn Business Card</title>
<link rel="stylesheet" href="https://fonts.googleapis.com/css2?family=Open+Sans:wght@400;600;700&display=swap">
<style>
  :root {
    --brand-blue: #1a6fba;
    --brand-blue-light: #2a82c8;
    --ink-grey: #4a4a4a;
    --title-grey: #7a7a7a;
    --paper: #ffffff;
    --backdrop: #262626;
  }
  * { box-sizing: border-box; margin: 0; padding: 0; }
  html, body { width: 1200px; height: 900px; overflow: hidden; }
  body {
    background: var(--backdrop);
    font-family: "Open Sans", Arial, sans-serif;
    position: relative;
  }
  .card {
    position: absolute;
    left: 290px;
    width: 620px;
    height: 354px;
    overflow: hidden;
  }
  .card-front {
    top: 70px;
    background: linear-gradient(160deg, var(--brand-blue) 0%, var(--brand-blue-light) 100%);
    color: var(--paper);
  }
  .brand-name {
    position: absolute;
    top: 118px;
    left: 0;
    width: 100%;
    text-align: center;
    font-size: 64px;
    font-weight: 400;
    letter-spacing: 10px;
    white-space: nowrap;
  }
  .street-address {
    position: absolute;
    bottom: 34px;
    width: 100%;
    text-align: center;
    font-size: 15px;
    letter-spacing: 0.5px;
  }
  .card-back {
    top: 476px;
    background: var(--paper);
  }
  .bottom-band {
    position: absolute;
    left: 0; right: 0; bottom: 0;
    height: 30px;
    background: var(--brand-blue);
  }
  .person {
    position: absolute;
    top: 116px;
    left: 20px;
    width: 215px;
    text-align: right;
    white-space: nowrap;
  }
  .person-name {
    color: var(--brand-blue);
    font-size: 26px;
    font-weight: 700;
    line-height: 1.15;
  }
  .person-title {
    color: var(--title-grey);
    font-size: 17px;
    font-weight: 400;
    margin-top: 2px;
  }
  .brand-mark {
    position: absolute;
    top: 146px;
    left: 252px;
    display: flex;
    align-items: center;
    gap: 6px;
    color: var(--brand-blue);
    font-size: 15px;
    font-weight: 600;
    white-space: nowrap;
  }
  .brand-dot {
    width: 12px; height: 12px;
    border-radius: 50%;
    background: var(--brand-blue);
  }
  .contact-list {
    position: absolute;
    top: 106px;
    left: 384px;
    list-style: none;
  }
  .contact-item {
    display: flex;
    align-items: center;
    gap: 9px;
    font-size: 16px;
    color: var(--ink-grey);
    line-height: 26px;
    white-space: nowrap;
  }
  .contact-icon { width: 15px; height: 15px; flex: none; }
  .site-name { color: var(--brand-blue); }
</style>
</head>
<body>
  <section class="card card-front">
    <div class="brand-name">QUILLBARN</div>
    <p class="street-address">your street address Northvale-1200</p>
  </section>

  <section class="card card-back">
    <div class="person">
      <div class="person-name">DANA WHITLOW</div>
      <div class="person-title">CEO/FOUNDER</div>
    </div>

    <div class="brand-mark"><span class="brand-dot"></span>QUILLBARN</div>

    <ul class="contact-list">
      <li class="contact-item">
        <svg class="contact-icon" viewBox="0 0 16 16"><circle cx="8" cy="8" r="8" fill="#1a6fba"/><rect x="5.5" y="3.5" width="5" height="9" rx="1" fill="none" stroke="#fff" stroke-width="1.3"/></svg>
        000 000 0000
      </li>
      <li class="contact-item">
        <svg class="contact-icon" viewBox="0 0 16 16"><circle cx="8" cy="8" r="8" fill="#1a6fba"/><path d="M5 4.5l2 .2.6 2-1 .9a5 5 0 0 0 2 2l.9-1 2 .6.2 2c-3.5.6-7.4-3.3-6.7-6.7z" fill="#fff"/></svg>
        000 000 0000
      </li>
      <li class="contact-item">
        <svg class="contact-icon" viewBox="0 0 16 16"><circle cx="8" cy="8" r="8" fill="#1a6fba"/><rect x="4" y="5" width="8" height="6" fill="#fff"/><path d="M4 5l4 3 4-3" fill="none" stroke="#1a6fba" stroke-width="1"/></svg>
        info@danawhitlow.com
      </li>
      <li class="contact-item">
        <svg class="contact-icon" viewBox="0 0 16 16"><circle cx="8" cy="8" r="8" fill="#1a6fba"/><circle cx="8" cy="8" r="4.2" fill="none" stroke="#fff" stroke-width="1.2"/><path d="M3.8 8h8.4M8 3.8c-2 2.4-2 6 0 8.4M8 3.8c2 2.4 2 6 0 8.4" fill="none" stroke="#fff" stroke-width="1"/></svg>
        <span>www.<span class="site-name">yoursitename</span>.com</span>
      </li>
    </ul>

    <div class="bottom-band"></div>
  </section>
</body>
</html>
```